Home page design for a live auction website.

Hi, we are looking at finding a good design for an auction website, only home page .. We will not be selling anything online, so the website will only be a portal where visitors can check about our company, upcoming auctions, online catalogues etc.
See attached our logo. Please use the same red that you see on the logo in the designs that you provide.
The final design should communicate high-end auction website, as we will be selling expensive piece of arts and antiques.
We should have a main frame where images of arts will circulate, with description of the art piece. just like on http://paris.vellmarotte-quisande.com/
(but with a better design overall) and of course a menu with different tabs, like "about us", "previous sales" "next sales", "contact" , "how to buy", "meet our specialists".

Target Market(s)

High end segment, who can afford to pay up to 250'000 for a piece of art

Industry/Entity Type

Online

Number of Pages Required

1 page

Requirements
Must have
• a frame with images rotating, just like on http://paris.vellmarotte-quisande.com/ . but the rest of the design should be more refined.
• we should also have a strong call to action, "Free online estimation", click here, estimation delivered in 48 hours"
Nice to have
• Tremaux Auctions, the brand should be well visible

```html
<!DOCTYPE html>
<html lang="en">
<head>
<meta charset="utf-8">
<title>Tremaux Auctions</title>
<link href="https://fonts.googleapis.com/css2?family=Roboto+Condensed:wght@400;700&family=Open+Sans:wght@400;600;700&display=swap" rel="stylesheet">
<style>
:root{
  --red:#c0272d;
  --red-dark:#9e1e23;
  --ink:#333;
  --muted:#777;
  --page:#efefef;
  --panel:#fff;
  --line:#e2e2e2;
  --footer:#2b2b2b;
  --footer-bottom:#1f1f1f;
  --footer-text:#a8a8a8;
}
*{margin:0;padding:0;box-sizing:border-box}
html,body{width:1200px;height:2224px;overflow:hidden}
body{background:var(--page);font-family:"Open Sans",Arial,sans-serif;color:var(--ink);font-size:12px;line-height:1.5}
.site-header{height:88px;background:#fff;display:flex;align-items:center;justify-content:space-between;padding:0 90px;border-bottom:1px solid var(--line)}
.brand{display:flex;align-items:center;gap:12px;font-family:"Roboto Condensed",Arial,sans-serif;font-weight:700;font-size:24px;color:var(--red);letter-spacing:1px;text-transform:uppercase}
.brand-mark{width:14px;height:14px;background:var(--red)}
.main-nav{display:flex;gap:34px;font-family:"Roboto Condensed",Arial,sans-serif;font-size:13px;text-transform:uppercase;color:#555;letter-spacing:.5px}
.main-nav a{color:inherit;text-decoration:none;padding:32px 0 30px;border-bottom:3px solid transparent}
.main-nav a.active{border-bottom-color:var(--red);color:var(--red)}
.hero{position:relative;height:502px;background:
  radial-gradient(circle at 12% 30%,#f2b24a 0,#c0501d 12%,transparent 26%),
  radial-gradient(circle at 35% 55%,#e8c15a 0,#a83a1a 14%,transparent 28%),
  radial-gradient(circle at 22% 80%,#d8472a 0,#7a1d14 14%,transparent 28%),
  radial-gradient(circle at 55% 25%,#f0d37a 0,#8f3318 12%,transparent 25%),
  radial-gradient(circle at 88% 45%,#e3c17a 0,#8a5a2a 14%,transparent 32%),
  linear-gradient(135deg,#3a1610,#5a2314 50%,#2a1410)}
.hero-card{position:absolute;left:620px;top:192px;width:320px;height:320px;border-radius:50%;background:rgba(255,255,255,.94);border:8px solid rgba(192,39,45,.85);display:flex;flex-direction:column;align-items:center;justify-content:center;text-align:center;padding:0 44px}
.hero-card h1{font-family:"Roboto Condensed",Arial,sans-serif;color:var(--red);font-size:24px;text-transform:uppercase;margin-bottom:12px}
.hero-card p{color:#555;font-size:12px;margin-bottom:16px}
.hero-card a{color:var(--red);font-family:"Roboto Condensed",Arial,sans-serif;font-weight:700;text-decoration:none;text-transform:uppercase;font-size:13px}
.hero-arrows{position:absolute;left:78px;bottom:22px;display:flex;gap:6px}
.arrow-btn{width:26px;height:26px;background:var(--red);display:flex;align-items:center;justify-content:center}
.columns{position:absolute;top:630px;left:90px;width:1020px;display:flex;gap:15px}
.panel{background:var(--panel);box-shadow:0 1px 4px rgba(0,0,0,.12);height:870px;padding:0 16px}
.panel-title{font-family:"Roboto Condensed",Arial,sans-serif;font-size:20px;font-weight:700;text-transform:uppercase;padding:12px 0 8px;border-bottom:2px solid var(--line);position:relative;margin-bottom:14px}
.panel-title::after{content:"";position:absolute;left:0;bottom:-2px;width:90px;height:2px;background:var(--red)}
.panel-title span{color:var(--red)}
.col-sales{width:320px}
.col-featured{width:340px}
.col-news{width:330px}
.sale-item{display:flex;gap:12px;padding:10px 0;border-bottom:1px solid var(--line);height:128px;align-items:flex-start}
.sale-thumb{width:96px;height:96px;flex:none}
.item-title{font-family:"Roboto Condensed",Arial,sans-serif;color:var(--red);font-size:13px;font-weight:700;text-transform:uppercase;margin-bottom:4px}
.item-text{color:var(--muted);font-size:11px;line-height:1.5}
.price{font-weight:700;color:var(--ink);margin-top:4px;font-size:12px}
.feature{margin-bottom:26px}
.feature-img{height:210px;margin-bottom:12px}
.read-more{color:var(--red);font-size:12px;display:block;margin-top:6px}
.news-item{display:flex;gap:14px;padding:14px 0;border-bottom:1px solid var(--line);height:160px}
.news-date{flex:none;width:52px;text-align:center;font-family:"Roboto Condensed",Arial,sans-serif;color:var(--red);line-height:1}
.news-date b{display:block;font-size:38px}
.news-date small{display:block;font-size:13px;text-transform:uppercase;color:#555;margin-top:4px}
.news-item .item-text{color:#444;font-size:12px}
.works{position:absolute;top:1525px;left:90px;width:1020px;height:370px;background:var(--panel);box-shadow:0 1px 4px rgba(0,0,0,.12);padding:0 16px}
.works-head{display:flex;justify-content:space-between;align-items:center}
.works-head .panel-title{flex:1}
.works-nav{position:absolute;right:16px;top:16px;display:flex;gap:4px}
.works-nav .arrow-btn{width:20px;height:20px;background:#999}
.works-grid{display:grid;grid-template-columns:repeat(4,1fr);gap:14px}
.work-img{height:200px;margin-bottom:10px}
.site-footer{position:absolute;top:1940px;left:0;width:1200px;height:284px;background:var(--footer);color:var(--footer-text)}
.footer-cols{display:flex;gap:60px;padding:30px 90px 0;height:240px}
.footer-col{flex:1}
.footer-col h3{font-family:"Roboto Condensed",Arial,sans-serif;color:#fff;font-size:18px;text-transform:uppercase;margin-bottom:14px;padding-bottom:8px;border-bottom:1px solid #444}
.footer-col p{font-size:11px;margin-bottom:8px}
.newsletter-input{width:100%;height:32px;background:#3a3a3a;border:1px solid #4a4a4a;color:#999;padding:0 10px;font-size:11px;display:flex;align-items:center;margin-bottom:12px}
.btn-subscribe{display:inline-block;background:var(--red);color:#fff;padding:8px 22px;font-size:11px;text-transform:uppercase;font-weight:700}
.footer-bottom{height:44px;background:var(--footer-bottom);display:flex;justify-content:space-between;align-items:center;padding:0 90px;font-size:11px}
.social{display:flex;align-items:center;gap:8px}
.social i{width:22px;height:22px;border-radius:50%;background:#555;display:block}
</style>
</head>
<body>
<header class="site-header">
  <div class="brand"><span class="brand-mark"></span>Tremaux Auctions</div>
  <nav class="main-nav">
    <a class="active" href="#">About us</a>
    <a href="#">Previous sales</a>
    <a href="#">Next sales</a>
    <a href="#">Contact</a>
    <a href="#">How to buy</a>
    <a href="#">Meet our specialists</a>
  </nav>
</header>

<section class="hero" role="img" aria-label="Slideshow photograph of glowing silk lanterns and an antique brass teapot">
  <div class="hero-card">
    <h1>Tremaux Auctions</h1>
    <p>Free online estimation of your artworks and antiques, delivered by our specialists within 48 hours.</p>
    <a href="#">Read more</a>
  </div>
  <div class="hero-arrows">
    <span class="arrow-btn"><svg width="10" height="10" viewBox="0 0 10 10"><path d="M7 1 3 5l4 4" stroke="#fff" stroke-width="2" fill="none"/></svg></span>
    <span class="arrow-btn"><svg width="10" height="10" viewBox="0 0 10 10"><path d="M3 1l4 4-4 4" stroke="#fff" stroke-width="2" fill="none"/></svg></span>
  </div>
</section>

<main class="columns">
  <section class="panel col-sales">
    <h2 class="panel-title">Forthcoming <span>Sales</span></h2>
    <article class="sale-item"><div class="sale-thumb" role="img" aria-label="Auction lot photograph" style="background:linear-gradient(135deg,#8a5a2e,#3b2414)"></div><div><h3 class="item-title">Neque porro quisquam</h3><p class="item-text">A rare piece from a private collection, offered at our next sale.</p><p class="price">£187.00</p></div></article>
    <article class="sale-item"><div class="sale-thumb" role="img" aria-label="Auction lot photograph" style="background:linear-gradient(135deg,#b08a5a,#5a3a20)"></div><div><h3 class="item-title">Neque porro quisquam</h3><p class="item-text">A rare piece from a private collection, offered at our next sale.</p><p class="price">£187.00</p></div></article>
    <article class="sale-item"><div class="sale-thumb" role="img" aria-label="Auction lot photograph" style="background:linear-gradient(135deg,#6e4a30,#2a1a10)"></div><div><h3 class="item-title">Neque porro quisquam</h3><p class="item-text">A rare piece from a private collection, offered at our next sale.</p><p class="price">£187.00</p></div></article>
    <article class="sale-item"><div class="sale-thumb" role="img" aria-label="Auction lot photograph" style="background:linear-gradient(135deg,#a0522d,#4a2210)"></div><div><h3 class="item-title">Neque porro quisquam</h3><p class="item-text">A rare piece from a private collection, offered at our next sale.</p><p class="price">£187.00</p></div></article>
    <article class="sale-item"><div class="sale-thumb" role="img" aria-label="Auction lot photograph" style="background:linear-gradient(135deg,#7a6a5a,#3a2e24)"></div><div><h3 class="item-title">Neque porro quisquam</h3><p class="item-text">A rare piece from a private collection, offered at our next sale.</p><p class="price">£187.00</p></div></article>
    <article class="sale-item"><div class="sale-thumb" role="img" aria-label="Auction lot photograph" style="background:linear-gradient(135deg,#c08850,#603818)"></div><div><h3 class="item-title">Neque porro quisquam</h3><p class="item-text">A rare piece from a private collection, offered at our next sale.</p><p class="price">£187.00</p></div></article>
  </section>

  <section class="panel col-featured">
    <h2 class="panel-title">Our <span>Featured</span></h2>
    <article class="feature">
      <div class="feature-img" role="img" aria-label="Painting of a lake with trees and mountains" style="background:linear-gradient(180deg,#8fb7d8,#5a8a6a 55%,#3a5a4a)"></div>
      <h3 class="item-title">Neque porro quisquam</h3>
      <p class="item-text">An exceptional painting presented in our featured selection, with full provenance and a condition report available from our specialists on request.</p>
      <a class="read-more" href="#">Read More</a>
    </article>
    <article class="feature">
      <div class="feature-img" role="img" aria-label="Painting of an autumn forest path" style="background:linear-gradient(180deg,#e8a03a,#c0501d 50%,#5a2a14)"></div>
      <h3 class="item-title">Neque porro quisquam</h3>
      <p class="item-text">An exceptional painting presented in our featured selection, with full provenance and a condition report available from our specialists on request.</p>
      <a class="read-more" href="#">Read More</a>
    </article>
  </section>

  <section class="panel col-news">
    <h2 class="panel-title">Recent <span>News</span></h2>
    <article class="news-item"><div class="news-date"><b>27</b><small>Sep</small></div><p class="item-text">Our autumn season opens with a major sale of paintings and furniture, viewing open all week in the Paris saleroom.</p></article>
    <article class="news-item"><div class="news-date"><b>27</b><small>Sep</small></div><p class="item-text">Our autumn season opens with a major sale of paintings and furniture, viewing open all week in the Paris saleroom.</p></article>
    <article class="news-item"><div class="news-date"><b>27</b><small>Sep</small></div><p class="item-text">Our autumn season opens with a major sale of paintings and furniture, viewing open all week in the Paris saleroom.</p></article>
    <article class="news-item"><div class="news-date"><b>27</b><small>Sep</small></div><p class="item-text">Our autumn season opens with a major sale of paintings and furniture, viewing open all week in the Paris saleroom.</p></article>
    <article class="news-item"><div class="news-date"><b>27</b><small>Sep</small></div><p class="item-text">Our autumn season opens with a major sale of paintings and furniture, viewing open all week in the Paris saleroom.</p></article>
  </section>
</main>

<section class="works">
  <h2 class="panel-title">Our <span>Works</span></h2>
  <div class="works-nav">
    <span class="arrow-btn"><svg width="8" height="8" viewBox="0 0 10 10"><path d="M7 1 3 5l4 4" stroke="#fff" stroke-width="2" fill="none"/></svg></span>
    <span class="arrow-btn"><svg width="8" height="8" viewBox="0 0 10 10"><path d="M3 1l4 4-4 4" stroke="#fff" stroke-width="2" fill="none"/></svg></span>
  </div>
  <div class="works-grid">
    <article><div class="work-img" role="img" aria-label="Engraved decorative artwork" style="background:linear-gradient(135deg,#b89a70,#5a4028)"></div><h3 class="item-title">Neque porro quisquam</h3><p class="item-text">A selection of works sold by our house in recent seasons.</p></article>
    <article><div class="work-img" role="img" aria-label="Ornamental carved artwork" style="background:linear-gradient(135deg,#d8c8a8,#7a6448)"></div><h3 class="item-title">Neque porro quisquam</h3><p class="item-text">A selection of works sold by our house in recent seasons.</p></article>
    <article><div class="work-img" role="img" aria-label="Antique metal object in close-up" style="background:linear-gradient(135deg,#9a8a74,#3a2e22)"></div><h3 class="item-title">Neque porro quisquam</h3><p class="item-text">A selection of works sold by our house in recent seasons.</p></article>
    <article><div class="work-img" role="img" aria-label="Black and white ink drawing" style="background:linear-gradient(135deg,#d8d8d8,#5a5a5a)"></div><h3 class="item-title">Neque porro quisquam</h3><p class="item-text">A selection of works sold by our house in recent seasons.</p></article>
  </div>
</section>

<footer class="site-footer">
  <div class="footer-cols">
    <div class="footer-col">
      <h3>About our company</h3>
      <p>Posted on March 18, 2024</p>
      <p>An independent Paris auction house for fine art, furniture and antiques, serving collectors for over forty years.</p>
      <p>Read more info</p>
    </div>
    <div class="footer-col">
      <h3>Newsletters</h3>
      <p>Subscribe for Our Newsletter</p>
      <div class="newsletter-input">Enter Your Email Id</div>
      <span class="btn-subscribe">Subscribe</span>
    </div>
    <div class="footer-col">
      <h3>Contact us</h3>
      <p>12 Rue Halvert, 75009 Paris, France</p>
      <p>+33 1 40 00 12 34</p>
      <p>info@tremaux-auctions.com</p>
    </div>
  </div>
  <div class="footer-bottom">
    <span>© 2024 Tremaux Auctions. All Rights Reserved.</span>
    <div class="social"><span>Connect with our social network</span><i></i><i></i><i></i><i></i></div>
  </div>
</footer>
</body>
</html>
```